New Book Cover Design Project for The Lantern Keeper

I need a book cover designed for my book, "Seven Quiet Paths to a Bigger Income, Leave the Office Behind, and Build the Life You Picture!" The cover needs to include my logo. It's a step by step guide to earning money from home in various different ways. By doing this, people can quit their jobs and live their dream life. A life with purpose, happiness and abundance. I would love an image of a lady in a suit crushing a desk, or of someone sitting on a island or of money abundantly flowing or a combination of all of these things. It needs to represent the dream life and be visually strong to look at. It needs to include the logo at the top. Its important that people identify with it instantly.
Updates

Project Deadline Extended Reason: I've extended the deadline as I realised I not provided some key details such as dimensions of the book, author's name plus details for the back cover. Thanks. Added Sunday, August 6, 2017

Target Market(s)

Women over 30 who are fed up with working in a cubicle and of corporate life.

Industry/Entity Type

Entrepreneur

Font styles to use
Other font styles liked:
• Arial Narrow or Century Gothic or something fun!

Colors

Designer to choose colors to be used in the design.

Requirements
Must have
• My logo at the top (non-negotiable). It needs to convey someone living their dreams or quitting their job or crushing their cubicle. I want it to be like no other title. Visually strong, clear and representative of what it is about. This book represents an opportunity for people to transform their lives! I want them to see this book and want to buy it.
Nice to have
• Examples could be leaving their desk and entering through a door to an amazing life. Money could feature somewhere in it. It needs to represent the dream and someone attaining it. It could feature balloons to escape their desk, or climbing out of their desk to an amazing life.
Should not have
• Anything scary! I don't want too many images or confusing images.

```html
<!DOCTYPE html>
<html lang="en">
<head>
<meta charset="utf-8">
<title>Seven Quiet Paths to a Bigger Income — Book Cover</title>
<link rel="stylesheet" href="https://fonts.googleapis.com/css2?family=Didact+Gothic&display=swap">
<style>
  :root {
    --cover-red: #bc1f24;
    --bubble-red: #e8343b;
    --ink-white: #ffffff;
    --brand-teal: #5bb4b7;
    --brand-grey: #8a8a8c;
    --money-light: #dcdad0;
    --money-dark: #8f9186;
  }
  * { margin: 0; padding: 0; box-sizing: border-box; }
  html, body {
    width: 795px; height: 1200px; overflow: hidden;
    background: var(--cover-red);
  }
  .cover {
    position: relative; width: 795px; height: 1200px; overflow: hidden;
    background: var(--cover-red);
    font-family: "Didact Gothic", "Century Gothic", sans-serif;
    color: var(--ink-white);
  }
  .speech-bubble { position: absolute; left: 0; top: 0; }
  .brand-plate {
    position: absolute; left: 181px; top: 27px; width: 435px; height: 159px;
    background: var(--ink-white);
    display: flex; align-items: center; justify-content: center; gap: 18px;
  }
  .brand-mark { width: 56px; height: 56px; background: var(--brand-grey); }
  .brand-name { font-size: 34px; color: var(--brand-teal); line-height: 1.1; }
  .title { position: absolute; left: 0; top: 0; width: 795px; height: 1200px; text-transform: uppercase; }
  .title-number {
    position: absolute; left: 82px; top: 318px;
    font-size: 118px; line-height: 1; letter-spacing: -2px;
  }
  .title-lead {
    position: absolute; left: 520px; top: 320px;
    font-size: 31px; line-height: 1.3;
  }
  .title-line { position: absolute; left: 0; width: 795px; text-align: center; }
  .title-line--quit { top: 540px; font-size: 42px; }
  .title-line--and { top: 620px; font-size: 27px; }
  .title-line--dream { top: 676px; font-size: 42px; }
  .money-shirts {
    position: absolute; left: 130px; top: 855px; width: 536px; height: 345px;
    background: linear-gradient(160deg, var(--money-light), var(--money-dark));
    border-radius: 40px 40px 0 0;
  }
</style>
</head>
<body>
<main class="cover">
  <svg class="speech-bubble" width="795" height="1200" viewBox="0 0 795 1200" aria-hidden="true">
    <path fill="var(--bubble-red)" d="M0,300 C120,235 300,222 450,225 C620,228 760,250 795,262 L795,770 C700,810 560,840 470,860 L400,900 L330,860 C200,840 80,800 0,770 Z"/>
  </svg>

  <header class="brand-plate">
    <span class="brand-mark"></span>
    <span class="brand-name">The Lantern Keeper</span>
  </header>

  <h1 class="title">
    <span class="title-number">Seven</span>
    <span class="title-lead">Quiet paths<br>to a bigger<br>income,</span>
    <span class="title-line title-line--quit">Leave the office behind,</span>
    <span class="title-line title-line--and">and</span>
    <span class="title-line title-line--dream">Build the life you picture!</span>
  </h1>

  <div class="money-shirts" role="img" aria-label="Two dollar bills folded into origami shirts, split apart at the bottom of the cover"></div>
</main>
</body>
</html>
```